Brindlewood Court Apartments Business Cards

We need a business card design for a small apartment community in the metro-Detroit area. The property has a park-like feel and is surrounded by trees and ponds.

The logo colors are:
R=9 G=117 B=127
R=210 G=183 B=114

Contact Information for Business Card

Marla Finch
Property Manager
Brindlewood Court Apartments
352 Brindlewood Way
Lake Orion, MI 48190
Phone (248)517-2039

```html
<!DOCTYPE html>
<html lang="en">
<head>
<meta charset="utf-8">
<title>Brindlewood Court Apartments — Business Cards</title>
<link rel="stylesheet" href="https://fonts.googleapis.com/css2?family=Montserrat:wght@500;600&family=Lato:wght@400&display=swap">
<style>
  :root {
    --backdrop: #2f2925;
    --card: #1a1a1b;
    --card-edge: #111112;
    --teal: #09757f;
    --gold: #d2b772;
    --white: #f2f2f2;
    --grey: #8d8f91;
    --tab-light: #e6e9ea;
  }
  * { margin: 0; padding: 0; box-sizing: border-box; }
  html, body {
    width: 1200px;
    height: 844px;
    overflow: hidden;
    background: var(--backdrop);
  }
  .canvas {
    position: relative;
    width: 1200px;
    height: 844px;
  }
  .card {
    position: absolute;
    top: 267px;
    width: 535px;
    height: 310px;
    background: var(--card);
    box-shadow: 0 10px 30px rgba(0,0,0,0.45);
    overflow: hidden;
  }

  /* ---------- contact side ---------- */
  .card-contact { left: 45px; }
  .band-top {
    position: absolute; left: 0; right: 0; top: 14px;
    height: 9px; background: var(--teal);
  }
  .band-bottom {
    position: absolute; left: 0; right: 0; bottom: 14px;
    height: 16px; background: var(--teal);
  }
  .identity {
    position: absolute;
    left: 205px; top: 78px;
    width: 220px;
  }
  .person-name {
    font-family: "Montserrat", sans-serif;
    font-weight: 600;
    font-size: 17px;
    letter-spacing: 0.5px;
    color: var(--white);
    text-transform: uppercase;
    padding-bottom: 4px;
    border-bottom: 1.5px solid var(--teal);
    display: inline-block;
    white-space: nowrap;
  }
  .person-title {
    font-family: "Lato", sans-serif;
    font-size: 14px;
    color: var(--grey);
    margin-top: 3px;
    margin-left: 24px;
    white-space: nowrap;
  }
  .contact-list {
    position: absolute;
    left: 0; right: 0; top: 158px;
    list-style: none;
    text-align: center;
    font-family: "Lato", sans-serif;
    font-size: 14px;
    line-height: 19px;
    color: var(--grey);
    padding-left: 110px;
    white-space: nowrap;
  }
  .address {
    position: absolute;
    left: 0; right: 0; bottom: 44px;
    text-align: center;
    font-family: "Lato", sans-serif;
    font-size: 14px;
    color: var(--grey);
    white-space: nowrap;
  }

  /* ---------- brand side ---------- */
  .card-brand { left: 620px; background: var(--card-edge); }
  .card-brand .face {
    position: absolute; inset: 0;
    background: var(--card);
  }
  .tab {
    position: absolute;
    width: 16px; height: 36px;
    background: var(--teal);
    border-left: 4px solid var(--tab-light);
  }
  .tab-top-right { right: 22px; top: 0; }
  .tab-left { left: 0; top: 150px; border-left: none; border-right: 4px solid var(--tab-light); }
  .brand-lockup {
    position: absolute;
    left: 0; right: 0; top: 95px;
    display: flex;
    flex-direction: column;
    align-items: center;
    gap: 14px;
  }
  .brand-mark {
    width: 46px; height: 46px;
    border-radius: 50%;
    background: var(--gold);
  }
  .brand-name {
    font-family: "Montserrat", sans-serif;
    font-weight: 600;
    font-size: 24px;
    letter-spacing: 2px;
    color: var(--gold);
    text-transform: uppercase;
    text-align: center;
    line-height: 1.25;
  }
</style>
</head>
<body>
<main class="canvas">

  <section class="card card-contact" aria-label="Business card, contact side">
    <div class="band-top"></div>
    <div class="identity">
      <p class="person-name">Marla Finch</p>
      <p class="person-title">Property Manager</p>
    </div>
    <ul class="contact-list">
      <li>(248)517-2039</li>
      <li>(248)517-2040</li>
      <li>office@brindlewoodcourt.com</li>
      <li>www.brindlewoodcourt.com</li>
    </ul>
    <p class="address">352 Brindlewood Way | Lake Orion, MI | 48190</p>
    <div class="band-bottom"></div>
  </section>

  <section class="card card-brand" aria-label="Business card, brand side">
    <div class="face"></div>
    <div class="tab tab-top-right"></div>
    <div class="tab tab-left"></div>
    <div class="brand-lockup">
      <div class="brand-mark"></div>
      <p class="brand-name">Brindlewood Court<br>Apartments</p>
    </div>
  </section>

</main>
</body>
</html>
```